Medical Practice Business Card

we need a business card for our new medical ophthalmology practice based in Needham Massachusetts. we are looking for a simple , modern and elegant design.
the card needs to contain the following
1- the logo of our practice (please see attached file)
2- the name of the practice : "Silver Birch Retina Care"
3- Doctor's Name: Tobias Rendell MD PhD
4- Specialty: Board-Certified Vitreoretinal Surgeon
5- practice address: 87 Larkspur Ave, Suite 210, Alder Falls VT 05481
7- Office number: 617- 482 - 7730
8- fax number: 617- 391 - 2268
9- email: info@sbretinahub.example
10- website: www.sbretinahub.example

```html
<!DOCTYPE html>
<html lang="en">
<head>
<meta charset="utf-8">
<title>Silver Birch Retina Care – Business Card</title>
<link href="https://fonts.googleapis.com/css2?family=Montserrat:wght@400;600;700&display=swap" rel="stylesheet">
<style>
  :root {
    --navy: #163a5f;
    --sky: #5aa9d6;
    --ink-grey: #6b6e72;
    --paper: #ffffff;
    --backdrop: #2a2b2d;
  }
  html, body {
    margin: 0;
    width: 1200px;
    height: 1200px;
    overflow: hidden;
    background: var(--backdrop);
    font-family: "Montserrat", Arial, sans-serif;
  }
  .stage {
    position: relative;
    width: 1200px;
    height: 1200px;
  }
  .card {
    position: absolute;
    top: 250px;
    width: 400px;
    height: 700px;
    border-radius: 26px;
    box-sizing: border-box;
    box-shadow: 0 10px 30px rgba(0,0,0,0.35);
  }
  .card--front {
    left: 160px;
    background: var(--paper);
    padding: 80px 32px 50px;
  }
  .card--back {
    left: 640px;
    background: var(--navy);
    display: flex;
    align-items: center;
    justify-content: center;
  }
  .brand {
    display: flex;
    align-items: center;
    gap: 12px;
    font-weight: 600;
    font-size: 27px;
    line-height: 1.15;
    letter-spacing: 0.5px;
    text-transform: uppercase;
  }
  .brand__dot {
    flex: none;
    width: 14px;
    height: 14px;
    border-radius: 50%;
    background: currentColor;
  }
  .card--front .brand { color: var(--navy); justify-content: center; }
  .card--back .brand { color: var(--paper); }
  .doctor {
    margin-top: 150px;
  }
  .doctor__name {
    margin: 0;
    font-size: 21px;
    font-weight: 700;
    color: var(--navy);
    letter-spacing: 0.3px;
    white-space: nowrap;
  }
  .doctor__name .credentials { color: var(--sky); }
  .doctor__title {
    margin: 6px 0 0;
    font-size: 15px;
    color: var(--ink-grey);
    letter-spacing: 0.3px;
    white-space: nowrap;
  }
  .address {
    margin-top: 44px;
    text-align: right;
    font-size: 17px;
    line-height: 1.5;
    color: var(--ink-grey);
    letter-spacing: 0.5px;
    font-style: normal;
  }
  .contacts {
    list-style: none;
    margin: 34px 0 0;
    padding: 0;
    text-align: right;
    font-size: 16px;
    line-height: 1.75;
    color: var(--ink-grey);
    letter-spacing: 0.3px;
  }
  .contacts li {
    display: flex;
    justify-content: flex-end;
    align-items: center;
    gap: 10px;
    white-space: nowrap;
  }
  .contacts svg {
    width: 15px;
    height: 15px;
    fill: var(--sky);
    flex: none;
  }
</style>
</head>
<body>
<main class="stage">
  <section class="card card--front" aria-label="Card front">
    <div class="brand"><span class="brand__dot"></span><span>Silver Birch<br>Retina Care</span></div>

    <div class="doctor">
      <h1 class="doctor__name">TOBIAS RENDELL <span class="credentials">MD PHD</span></h1>
      <p class="doctor__title">Board-Certified Vitreoretinal Surgeon</p>
    </div>

    <address class="address">87 Larkspur Ave, Suite 210<br>Alder Falls VT 05481</address>

    <ul class="contacts">
      <li>617- 482 - 7730
        <svg viewBox="0 0 24 24" aria-label="Phone"><path d="M6.6 10.8a15 15 0 0 0 6.6 6.6l2.2-2.2a1 1 0 0 1 1-.25 11.4 11.4 0 0 0 3.6.57 1 1 0 0 1 1 1V20a1 1 0 0 1-1 1A17 17 0 0 1 3 4a1 1 0 0 1 1-1h3.5a1 1 0 0 1 1 1c0 1.25.2 2.45.57 3.570a1 1 0 0 1-.25 1z"/></svg>
      </li>
      <li>617- 391 - 2268
        <svg viewBox="0 0 24 24" aria-label="Fax"><path d="M7 3h10v5H7zM4 9h16a2 2 0 0 1 2 2v6h-4v4H6v-4H2v-6a2 2 0 0 1 2-2zm4 7v3h8v-3z"/></svg>
      </li>
      <li>info@sbretinahub.example
        <svg viewBox="0 0 24 24" aria-label="Email"><path d="M2 5h20v14H2zm2 2v.5l8 5 8-5V7l-8 5z"/></svg>
      </li>
      <li>www.sbretinahub.example
        <svg viewBox="0 0 24 24" aria-label="Website"><path d="M12 2a10 10 0 1 0 0 20 10 10 0 0 0 0-20zm0 2c.9 1.2 1.6 2.6 2 4h-4c.4-1.4 1.1-2.8 2-4zM4.3 14a8 8 0 0 1 0-4h3.4a16 16 0 0 0 0 4zm.9 2h3a14 14 0 0 0 1.3 3.3A8 8 0 0 1 5.2 16zm3-8h-3a8 8 0 0 1 4.3-3.3A14 14 0 0 0 8.2 8zM12 20c-.9-1.2-1.600-2.6-2-4h4c-.4 1.4-1.1 2.8-2 4zm2.3-6H9.7a14 14 0 0 1 0-4h4.6a14 14 0 0 1 0 4zm.2 5.3A14 14 0 0 0 15.8 16h3a8 8 0 0 1-4.3 3.3zM16.3 14a16 16 0 0 0 0-4h3.4a8 8 0 0 1 0 4zm-.5-6a14 14 0 0 0-1.3-3.3A8 8 0 0 1 18.8 8z"/></svg>
      </li>
    </ul>
  </section>

  <section class="card card--back" aria-label="Card back">
    <div class="brand"><span class="brand__dot"></span><span>Silver Birch<br>Retina Care</span></div>
  </section>
</main>
</body>
</html>
```